Info Graphic for Radiant Current Academy

WELCOME To The Radiant Current Academy (RCA)

We are wanting to create a visual info graphic display of a newly designed transformational pathway program.

Please display the following heading:

The Radiant Current Academy (RCA) Pathway Program

Subheading:

“Feeling alive and living the life you want to be living.”

Please display each step along the path clearly and with visuals representations that reflect the energy of the word and achievement accomplished.

We would like to display each step individually whilst tying to capture a flow of progression whilst maintaining the look and feel of each step.

The infographic design wants to really spark people’s attention, create impact and a curiosity resulting in a desire to seek more information regarding the program.

Energetic vibrant colours and flow are a must.

A sense of Playfulness, fun and energy is what we are looking for with this design.

The pathway is progressive with each step building on the last and I would like this to be represented in a linear fashion and NOT show steps as hierarchical.

The below documents the steps in order of progression and describes the key focus and outcome for each of the steps.

THE RCA PATHWAY:

Step 1: Intriguing You - Discover the path to transformation and igniting your relationships and life.

Step 2: Energizing You - Introduction to the Foundational principles.

Step 3: Awakening You - Creating juicy, deep connections with self and others.

Step 4: Transforming You - Feeling alive and creating a life of clarity and flow.

Step 5: Igniting You - Discovering that “This S**T Works” by living the life you want to be living.

Additional Modules available at Transforming You (by invitation)

Additional Step: Launching You - Learn to share the principles and tools to facilitate the RCA Path for family, friends and clients.

Additional Step: Aligning You - How do couples co-create a relationship that is on fire with passion and expression?

I have attached a previous style guide that we have utilised however don’t want to be limited to just this in the designs.

Happy for this to be utilised and included in designs and we are very open to do something completely different, please be creative.

Any questions or further information required, please let me know.
Updates

Target Market(s)

People looking to Feel alive and living the life you want to be living

Industry/Entity Type

Relationship and Personal Development

Requirements
Must have
• Creativity
Nice to have
• Linear display of steps and the explanations at each step included in the description
Should not have
• display hierarchy

```html
<!DOCTYPE html>
<html lang="en">
<head>
<meta charset="utf-8">
<title>Radiant Current Academy (RCA) Pathway Program</title>
<link href="https://fonts.googleapis.com/css2?family=Montserrat:wght@300;400;600;700&display=swap" rel="stylesheet">
<style>
  :root {
    --ink: #111111;
    --text: #222222;
    --violet: #7209e0;
    --lilac: #c9a9ee;
    --paper: #ffffff;
    --icon-tone: #262626;
  }
  html, body {
    margin: 0;
    padding: 0;
    overflow: hidden;
    background: var(--paper);
  }
  .canvas {
    position: relative;
    width: 1200px;
    height: 524px;
    overflow: hidden;
    background: var(--paper);
    font-family: "Montserrat", sans-serif;
    color: var(--ink);
  }
  .program-title {
    position: absolute;
    top: 52px;
    left: 0;
    width: 100%;
    margin: 0;
    text-align: center;
    font-weight: 700;
    font-size: 40px;
    line-height: 41px;
    letter-spacing: 0.5px;
  }
  .program-tagline {
    position: absolute;
    top: 149px;
    left: 0;
    width: 100%;
    margin: 0;
    text-align: center;
    font-weight: 300;
    font-size: 22.5px;
    letter-spacing: 0.4px;
  }
  .pathway-graphics {
    position: absolute;
    inset: 0;
  }
  .ring-outer { fill: none; stroke: var(--violet); stroke-width: 2.4; }
  .ring-inner { fill: none; stroke: var(--lilac); stroke-width: 11.5; }
  .ring-base { fill: none; stroke: var(--violet); stroke-width: 11; }
  .stem-dot { fill: var(--violet); }
  .step-icon { fill: var(--icon-tone); }
  .step {
    position: absolute;
    top: 410px;
    width: 180px;
    margin-left: -90px;
    text-align: center;
  }
  .step-name {
    margin: 0 0 3px;
    font-weight: 600;
    font-size: 13.3px;
    letter-spacing: 0.3px;
    white-space: nowrap;
  }
  .step-text {
    margin: 0;
    font-weight: 400;
    font-size: 9px;
    line-height: 11.8px;
    color: var(--text);
  }
</style>
</head>
<body>
<main class="canvas">
  <h1 class="program-title">THE RADIANT CURRENT ACADEMY<br>(RCA) PATHWAY PROGRAM</h1>
  <p class="program-tagline">FEELING ALIVE AND LIVING THE LIFE YOU WANT TO BE LIVING</p>

  <svg class="pathway-graphics" width="1200" height="524" viewBox="0 0 1200 524" aria-hidden="false">
    <defs>
      <g id="step-marker">
        <path class="ring-outer" d="M -77 287 A 77 77 0 1 1 0 364 L 0 377"/>
        <circle class="stem-dot" cx="0" cy="381" r="4.2"/>
        <path class="ring-inner" d="M -50.6 331 A 67 67 0 1 1 50.6 331"/>
        <path class="ring-base" d="M 38.6 333 A 60 60 0 0 1 -38.6 333"/>
      </g>
    </defs>
    <g transform="translate(234 0)">
      <use href="#step-marker"/>
      <rect class="step-icon" x="-22" y="258" width="44" height="60" rx="8" role="img" aria-label="Icon: group of people with a sparking idea cloud"/>
    </g>
    <g transform="translate(416 0)">
      <use href="#step-marker"/>
      <rect class="step-icon" x="-28" y="256" width="56" height="60" rx="8" role="img" aria-label="Icon: person standing on a podium with arms raised"/>
    </g>
    <g transform="translate(603 0)">
      <use href="#step-marker"/>
      <rect class="step-icon" x="-25" y="258" width="50" height="48" rx="8" role="img" aria-label="Icon: person framed by upward arrows"/>
    </g>
    <g transform="translate(789 0)">
      <use href="#step-marker"/>
      <rect class="step-icon" x="-26" y="253" width="52" height="58" rx="8" role="img" aria-label="Icon: three people together with a burst above"/>
    </g>
    <g transform="translate(975 0)">
      <use href="#step-marker"/>
      <rect class="step-icon" x="-36" y="254" width="72" height="59" rx="8" role="img" aria-label="Icon: person beside a target hit by an arrow"/>
    </g>
  </svg>

  <section class="step" style="left:233px">
    <h2 class="step-name">INTRIGUING YOU</h2>
    <p class="step-text">Discover the path to<br>transformation and igniting<br>your relationships and life.</p>
  </section>
  <section class="step" style="left:420px">
    <h2 class="step-name">ENERGIZING YOU</h2>
    <p class="step-text">Introduction to the<br>Foundational principles</p>
  </section>
  <section class="step" style="left:606px">
    <h2 class="step-name">AWAKENING YOU</h2>
    <p class="step-text">Creating juicy,<br>deep connections with<br>self and others.</p>
  </section>
  <section class="step" style="left:792px">
    <h2 class="step-name">TRANSFORMING YOU</h2>
    <p class="step-text">Feeling alive and<br>creating a life of clarity<br>and flow.</p>
  </section>
  <section class="step" style="left:974px">
    <h2 class="step-name">IGNITING YOU</h2>
    <p class="step-text">Discovering that<br>“This S**T Works” by living<br>the life you want to be living.</p>
  </section>
</main>
</body>
</html>
```